Renata Quisby

Luxury And Style -

Black - White & Gold

Target Market(s)

Fashion

Industry/Entity Type

Fashion

Requirements
Must have
• High-End
Nice to have
• We will Print on Silk Paper

```html
<!DOCTYPE html>
<html lang="en">
<head>
<meta charset="utf-8">
<title>Renata Quisby — Letterhead</title>
<link href="https://fonts.googleapis.com/css2?family=Marcellus&display=swap" rel="stylesheet">
<style>
  :root {
    --tan: #c19b6e;
    --navy: #00021f;
    --gold: #c9a46e;
    --paper: #ffffff;
  }
  html, body {
    margin: 0;
    padding: 0;
    overflow: hidden;
    background: var(--paper);
  }
  .letterhead {
    position: relative;
    width: 848px;
    height: 1200px;
    background: var(--paper);
    overflow: hidden;
  }
  .header-band {
    position: absolute;
    top: 0;
    left: 0;
    width: 848px;
    height: 193px;
    background: var(--tan);
  }
  .brand-block {
    position: absolute;
    top: 0;
    left: 71px;
    width: 270px;
    height: 193px;
    background: var(--navy);
    display: flex;
    flex-direction: column;
    align-items: center;
    justify-content: center;
    gap: 16px;
  }
  .brand-dot {
    width: 10px;
    height: 10px;
    border-radius: 50%;
    background: var(--gold);
  }
  .brand-name {
    margin: 0;
    font-family: "Marcellus", serif;
    font-weight: 400;
    font-size: 22px;
    letter-spacing: 4px;
    text-transform: uppercase;
    color: var(--gold);
  }
  .footer-bar {
    position: absolute;
    left: 0;
    bottom: 0;
    width: 848px;
    height: 32px;
    background: var(--navy);
    border-radius: 36px 36px 0 0;
  }
</style>
</head>
<body>
  <div class="letterhead">
    <header class="header-band">
      <div class="brand-block">
        <span class="brand-dot"></span>
        <p class="brand-name">Renata Quisby</p>
      </div>
    </header>
    <footer class="footer-bar"></footer>
  </div>
</body>
</html>
```